Software company seeking fresh website design

Using an already existing logo create a fresh, clean and professional web design for our company "Byte Lantern". Byte Lantern focuses on making business better through system integrations and software product development.

We're looking for a web design which has layouts for the following pages:
- Home Page
- Team Page
- Case Studies
- Market (List of Products)
- Product Page (Individual Product Details)
- About Page
- Media Page

Some websites and designs we'd like you to take inspiration from:
- Quillor.com
- https://www.portfolux.net/gallery/71830256/Taskly-redesign
- https://pixelnook.com/shots/5817362-Full-Range-Website-Design-for-a-Software-Company

Ideally the design should communicate an enterprise-level business with years of experience that can be trusted to deliver on budget and on-time.

Target Market(s)

Medium to High-Level Enterprise

Industry/Entity Type

Software Development

Coding

Coded - Design and coding required

Number of Pages Required

5+ page

Font styles to use
Sans Serif

Colors

Designer to choose colors to be used in the design.

Requirements
Must have
• - High Level of Professionalism
• - Be a unique design
• - Come with well-formatted and organised html + css + javascript
• - Must work on ie9, latest Chrome, latest Firefox, latest safari. iPhone6 and Android
• - Must be a progressive template
• - Must incorporate logo colors or at least be compatible with them
Nice to have
• - Hero, an area to display things we're proud of but look good without that area if need be.
• - Juicy animations that are performant and degrade nicely
Should not have
• - Submission must not be a template re-branded for the business

```html
<!DOCTYPE html>
<html lang="en">
<head>
<meta charset="utf-8">
<title>Byte Lantern</title>
<link rel="stylesheet" href="https://fonts.googleapis.com/css2?family=Lato:wght@400;700;900&family=Open+Sans:wght@400;600;700&display=swap">
<style>
:root{
  --brand:#ef4e23;
  --brand-dark:#d63f17;
  --ink:#1d1d1d;
  --text:#555;
  --muted:#777;
  --white:#fff;
  --band:#ececec;
  --footer:#f3f3f3;
  --line:#d9d9d9;
  --frame:#bdbdbd;
}
*{box-sizing:border-box;margin:0;padding:0}
html,body{width:1200px;height:2517px;overflow:hidden;background:var(--white)}
body{font-family:"Open Sans",Arial,sans-serif;color:var(--text)}
.page{position:relative;width:1200px;height:2517px;overflow:hidden}
.abs{position:absolute}
.hero-bg{position:absolute;left:0;top:0;width:1200px;height:680px}
.brand-name{font-family:"Lato",sans-serif;font-weight:700;color:var(--white);font-size:34px;display:flex;align-items:center;gap:12px;white-space:nowrap}
.brand-name .mark{width:22px;height:22px;background:var(--white);border-radius:50%}
.nav{position:absolute;top:36px;left:356px;display:flex;gap:27px;font-family:"Lato",sans-serif;font-weight:700;font-size:16px;color:var(--white)}
.nav .active{color:#ffd33d}
.nav-search{position:absolute;left:961px;top:38px}
.login-btn{position:absolute;left:1006px;top:30px;width:96px;height:38px;border:2px solid var(--white);border-radius:20px;color:var(--white);font-family:"Lato",sans-serif;font-weight:700;font-size:15px;display:flex;align-items:center;justify-content:center;gap:6px}
.hero-title{left:98px;top:205px;font-family:"Lato",sans-serif;font-size:62px;color:var(--white);font-weight:400;line-height:1}
.hero-title b{font-weight:900}
.hero-text{left:99px;top:294px;width:480px;font-size:18.5px;line-height:31px;color:var(--white)}
.btn-outline{left:100px;top:423px;width:161px;height:52px;border:2px solid var(--white);border-radius:26px;color:var(--white);font-family:"Lato",sans-serif;font-weight:700;font-size:16px;display:flex;align-items:center;justify-content:center}
.hero-art{left:580px;top:92px;width:528px;height:420px;border-radius:20px;background:radial-gradient(circle at 45% 50%,#2b2f3a 0%,#3a3d48 35%,rgba(214,63,23,.6) 70%,rgba(239,78,35,0) 100%)}
.welcome-frame{left:498px;top:690px;width:601px;height:454px;border:1.5px solid var(--frame)}
.welcome-photo{left:99px;top:753px;width:482px;height:326px;background:linear-gradient(135deg,#c7b99a 0%,#8b8c86 45%,#4d4f55 100%);box-shadow:0 2px 6px rgba(0,0,0,.2)}
.play{left:310px;top:886px}
.section-title{font-family:"Lato",sans-serif;font-size:40px;color:var(--ink);font-weight:400;line-height:1}
.section-title b{font-weight:900}
.welcome-title{left:615px;top:757px}
.welcome-text{left:616px;top:823px;width:450px;font-size:14.5px;line-height:28px;color:var(--text)}
.btn-solid{background:var(--brand);color:var(--white);border-radius:24px;font-family:"Lato",sans-serif;font-weight:700;font-size:15px;display:flex;align-items:center;justify-content:center}
.welcome-btn{left:617px;top:1025px;width:135px;height:44px}
.services-band{left:0;top:1240px;width:1200px;height:455px;background:var(--band)}
.services-title{left:0;width:1200px;top:1300px;text-align:center}
.service{position:absolute;top:1395px;width:270px;text-align:center}
.service-icon{height:86px;display:flex;align-items:center;justify-content:center}
.service h3{font-family:"Lato",sans-serif;font-weight:700;font-size:22px;color:var(--ink);margin-top:30px}
.service p{font-size:13.5px;line-height:25px;color:var(--muted);margin-top:8px}
.read-more{font-family:"Lato",sans-serif;font-weight:900;font-size:14px;color:var(--brand);letter-spacing:.2px}
.service .read-more{margin-top:12px;display:block}
.blog-title{left:0;width:1200px;top:1782px;text-align:center}
.post-photo{position:absolute;top:1874px;width:218px;height:187px;border:4px solid var(--white);box-shadow:0 1px 5px rgba(0,0,0,.25)}
.post-photo.one{left:99px;background:linear-gradient(135deg,#8ea3bf 0%,#3f5775 55%,#1e2c40 100%)}
.post-photo.two{left:623px;background:linear-gradient(135deg,#d3d3d3 0%,#8a8a8a 50%,#3b3b3b 100%)}
.post-body{position:absolute;top:1870px;width:245px}
.post-body h4{font-family:"Lato",sans-serif;font-weight:700;font-size:21.5px;color:var(--ink);white-space:nowrap}
.post-meta{font-size:12.5px;color:#444;margin-top:10px;display:flex;align-items:center;gap:6px}
.post-meta .sep{margin:0 4px}
.post-body p{font-size:12.5px;line-height:24.5px;color:#444;margin-top:12px}
.post-body .read-more{display:block;margin-top:12px}
.footer{left:0;top:2156px;width:1200px;height:361px;background:var(--footer)}
.footer-brand{left:99px;top:2340px;font-family:"Lato",sans-serif;font-weight:700;font-size:40px;color:var(--brand);display:flex;align-items:center;gap:12px;white-space:nowrap}
.footer-brand .mark{width:24px;height:24px;background:var(--brand);border-radius:50%}
.footer-col h5{font-family:"Lato",sans-serif;font-weight:700;font-size:19.5px;color:var(--ink)}
.footer-links{list-style:none;margin-top:16px;font-size:12.5px;line-height:22.5px;color:#333}
.newsletter-text{margin-top:16px;font-size:12.5px;line-height:21px;color:#333;width:230px}
.email-field{margin-top:12px;width:253px;height:34px;background:var(--white);border-bottom:2px solid var(--line);font-size:11.5px;color:#999;padding:9px 12px}
.subscribe{margin-top:18px;width:99px;height:29px;border:1.5px solid var(--brand-dark);border-radius:15px;color:var(--brand-dark);font-family:"Lato",sans-serif;font-weight:900;font-size:12px;display:flex;align-items:center;justify-content:center}
.contact-item{position:absolute;left:945px;display:flex;gap:14px;font-size:12.5px;line-height:21px;color:#333}
.divider{left:99px;top:2435px;width:1000px;height:1px;background:var(--line)}
.copyright{left:99px;top:2466px;font-size:12px;color:#333}
.social{position:absolute;top:2462px;width:27px;height:27px;border:1.5px solid var(--brand);border-radius:50%}
</style>
</head>
<body>
<div class="page">

  <header>
    <svg class="hero-bg" viewBox="0 0 1200 680" aria-hidden="true">
      <polygon points="0,0 1200,0 1200,361 75,676 151,559 0,604" fill="#ef4e23"/>
    </svg>
    <div class="abs brand-name" style="left:100px;top:90px"><span class="mark"></span>Byte Lantern</div>
    <nav class="nav">
      <span class="active">Home</span><span>About us</span><span>Services</span><span>Products</span><span>Developers</span><span>Blog</span><span>Contact us</span>
    </nav>
    <svg class="nav-search" width="18" height="18" viewBox="0 0 18 18" aria-hidden="true"><circle cx="7" cy="7" r="5.5" fill="none" stroke="#fff" stroke-width="2.4"/><line x1="11" y1="11" x2="16" y2="16" stroke="#fff" stroke-width="2.6" stroke-linecap="round"/></svg>
    <div class="login-btn"><svg width="11" height="13" viewBox="0 0 11 13" aria-hidden="true"><rect x="0" y="5.5" width="11" height="7.5" rx="1" fill="#fff"/><path d="M2.5 5.5V4a3 3 0 0 1 6 0v1.5" fill="none" stroke="#fff" stroke-width="1.8"/></svg>LOGIN</div>

    <h1 class="abs hero-title"><b>Byte</b> Lantern</h1>
    <p class="abs hero-text">Byte Lantern is a software company focuses on making business better through system integrations and software product development.</p>
    <div class="abs btn-outline">GET A QUOTE</div>
    <div class="abs hero-art" role="img" aria-label="Illustration of a laptop with code, a clock, gears, tools and language badges"></div>
  </header>

  <section class="welcome">
    <div class="abs welcome-frame"></div>
    <div class="abs welcome-photo" role="img" aria-label="Photo of hands typing on a laptop at a desk"></div>
    <svg class="abs play" width="60" height="60" viewBox="0 0 60 60" aria-hidden="true"><circle cx="30" cy="30" r="28" fill="#1d1d1d" stroke="#fff" stroke-width="2"/><polygon points="24,18 24,42 43,30" fill="#fff"/></svg>
    <h2 class="abs section-title welcome-title"><b>Welcome to</b> Byte Lantern</h2>
    <p class="abs welcome-text">Nemo enim ipsam voluptatem quia voluptas sit aspernatur aut oditaut fugit, sed quia consequuntur magni dolores eos qui ratione voluptate m sequi nesciun porro quisquam est, qui dolorem ipsum quia dolor sit amet, consectetur, adipisci velit, sed quia non numquam eius modtem pora incidunt ut labore et dolore magnam aliquam quaerat voluptatet enim ad minima veniam, quis nostrum.</p>
    <div class="abs btn-solid welcome-btn">READ MORE</div>
  </section>

  <section class="services">
    <div class="abs services-band"></div>
    <h2 class="abs section-title services-title"><b>What</b> We Do</h2>

    <div class="service" style="left:73px">
      <div class="service-icon"><svg width="78" height="66" viewBox="0 0 78 66" aria-hidden="true"><path d="M27 12V6a4 4 0 0 1 4-4h16a4 4 0 0 1 4 4v6" fill="none" stroke="#ef4e23" stroke-width="5"/><rect x="0" y="12" width="78" height="54" rx="6" fill="#ef4e23"/><rect x="14" y="12" width="4" height="54" fill="#ececec"/><rect x="60" y="12" width="4" height="54" fill="#ececec"/></svg></div>
      <h3>Consulting</h3>
      <p>At vero eos et accusamus et iusto odio dignissimos ducimus qui bla</p>
      <span class="read-more">READ MORE</span>
    </div>
    <div class="service" style="left:333px">
      <div class="service-icon"><svg width="86" height="80" viewBox="0 0 86 80" aria-hidden="true" fill="#ef4e23"><g transform="translate(30,44)"><circle r="20"/><g><rect x="-6" y="-30" width="12" height="60" rx="2"/><rect x="-6" y="-30" width="12" height="60" rx="2" transform="rotate(45)"/><rect x="-6" y="-30" width="12" height="60" rx="2" transform="rotate(90)"/><rect x="-6" y="-30" width="12" height="60" rx="2" transform="rotate(135)"/></g><circle r="8" fill="#ececec"/></g><g transform="translate(68,20)"><circle r="11"/><rect x="-4" y="-17" width="8" height="34" rx="1"/><rect x="-4" y="-17" width="8" height="34" rx="1" transform="rotate(60)"/><rect x="-4" y="-17" width="8" height="34" rx="1" transform="rotate(120)"/><circle r="4.5" fill="#ececec"/></g><g transform="translate(70,62)"><circle r="9"/><rect x="-3.5" y="-14" width="7" height="28" rx="1"/><rect x="-3.5" y="-14" width="7" height="28" rx="1" transform="rotate(60)"/><rect x="-3.5" y="-14" width="7" height="28" rx="1" transform="rotate(120)"/><circle r="3.5" fill="#ececec"/></g></svg></div>
      <h3>Development services</h3>
      <p>At vero eos et accusamus et iusto odio dignissimos ducimus qui bla</p>
      <span class="read-more">READ MORE</span>
    </div>
    <div class="service" style="left:593px">
      <div class="service-icon"><svg width="62" height="72" viewBox="0 0 62 72" aria-hidden="true" fill="#ef4e23"><circle cx="31" cy="17" r="17"/><path d="M0 72V56a16 16 0 0 1 16-16h30a16 16 0 0 1 16 16v16z"/></svg></div>
      <h3>Expert services</h3>
      <p>At vero eos et accusamus et iusto odio dignissimos ducimus qui bla</p>
      <span class="read-more">READ MORE</span>
    </div>
    <div class="service" style="left:853px">
      <div class="service-icon"><svg width="72" height="62" viewBox="0 0 72 62" aria-hidden="true"><path d="M8 42V36a28 28 0 0 1 56 0v6" fill="none" stroke="#ef4e23" stroke-width="8"/><rect x="0" y="32" width="18" height="30" rx="6" fill="#ef4e23"/><rect x="54" y="32" width="18" height="30" rx="6" fill="#ef4e23"/></svg></div>
      <h3>Support services</h3>
      <p>At vero eos et accusamus et iusto odio dignissimos ducimus qui bla</p>
      <span class="read-more">READ MORE</span>
    </div>
  </section>

  <section class="blog">
    <h2 class="abs section-title blog-title"><b>Latest</b> Blog</h2>

    <div class="post-photo one" role="img" aria-label="Photo of a business team reviewing charts on a tablet"></div>
    <article class="post-body" style="left:343px">
      <h4>At vero eos et accu samu</h4>
      <div class="post-meta"><svg width="11" height="11" viewBox="0 0 11 11" aria-hidden="true"><rect x="0" y="1.5" width="11" height="9.5" rx="1" fill="#ef4e23"/><rect x="1.5" y="4" width="8" height="5.5" fill="#fff"/></svg>17/08/2017<span class="sep">|</span><svg width="10" height="11" viewBox="0 0 10 11" aria-hidden="true" fill="#ef4e23"><circle cx="5" cy="3" r="3"/><path d="M0 11V9a3 3 0 0 1 3-3h4a3 3 0 0 1 3 3v2z"/></svg>Mara Quist</div>
      <p>Temporibus autem quibusdam et aut offi ciis debitis aut rerum necessitatibus sae pe eveniet ut et voluptates.</p>
      <span class="read-more">READ MORE</span>
    </article>

    <div class="post-photo two" role="img" aria-label="Photo of hands holding printed reports beside a keyboard"></div>
    <article class="post-body" style="left:869px">
      <h4>At vero eos et accu samu</h4>
      <div class="post-meta"><svg width="11" height="11" viewBox="0 0 11 11" aria-hidden="true"><rect x="0" y="1.5" width="11" height="9.5" rx="1" fill="#ef4e23"/><rect x="1.5" y="4" width="8" height="5.5" fill="#fff"/></svg>17/08/2017<span class="sep">|</span><svg width="10" height="11" viewBox="0 0 10 11" aria-hidden="true" fill="#ef4e23"><circle cx="5" cy="3" r="3"/><path d="M0 11V9a3 3 0 0 1 3-3h4a3 3 0 0 1 3 3v2z"/></svg>Mara Quist</div>
      <p>Temporibus autem quibusdam et aut offi ciis debitis aut rerum necessitatibus sae pe eveniet ut et voluptates.</p>
      <span class="read-more">READ MORE</span>
    </article>
  </section>

  <footer>
    <div class="abs footer"></div>
    <div class="abs footer-brand"><span class="mark"></span>Byte Lantern</div>

    <div class="abs footer-col" style="left:440px;top:2232px">
      <h5>Information</h5>
      <ul class="footer-links"><li>Home</li><li>About Us</li><li>Services</li><li>Blog</li><li>Career</li><li>Contact Us</li></ul>
    </div>
    <div class="abs footer-col" style="left:628px;top:2232px">
      <h5>Newsletter Subscription</h5>
      <p class="newsletter-text">Register your Email Address to get Information about us</p>
      <div class="email-field">Email Address</div>
      <div class="subscribe">SUBSCRIBE</div>
    </div>
    <div class="abs footer-col" style="left:945px;top:2232px"><h5>Contact Us</h5></div>
    <div class="contact-item" style="top:2274px"><svg width="11" height="15" viewBox="0 0 11 15" aria-hidden="true"><path d="M5.5 0A5.5 5.5 0 0 0 0 5.5C0 9.5 5.5 15 5.5 15S11 9.5 11 5.5A5.5 5.5 0 0 0 5.5 0z" fill="#ef4e23"/><circle cx="5.5" cy="5.5" r="2" fill="#f3f3f3"/></svg><span style="margin-left:10px">Kestrel Lane 12<br>4021 Norvale</span></div>
    <div class="contact-item" style="top:2334px"><svg width="14" height="14" viewBox="0 0 14 14" aria-hidden="true"><path d="M3 0l3 3-2 2c1 2 3 4 5 5l2-2 3 3-2 3C6 14 0 8 0 3z" fill="#ef4e23"/></svg><span style="margin-left:7px">1 555 014 2290</span></div>
    <div class="contact-item" style="top:2373px"><svg width="15" height="11" viewBox="0 0 15 11" aria-hidden="true"><rect width="15" height="11" rx="1" fill="#ef4e23"/><path d="M0.5 1l7 5 7-5" fill="none" stroke="#f3f3f3" stroke-width="1.3"/></svg><span style="margin-left:6px">info@bytelantern.com</span></div>

    <div class="abs divider"></div>
    <p class="abs copyright">Copyrights © 2017, Byte Lantern. All rights reserved.</p>
    <span class="social" style="left:976px"></span>
    <span class="social" style="left:1008px"></span>
    <span class="social" style="left:1040px"></span>
    <span class="social" style="left:1073px"></span>
  </footer>

</div>
</body>
</html>
```